Larkspur Homes - wanted BRILLIANT website design for our new property investing company

We need a website design for our new company based in Bristol, England, UK called "Larkspur Homes". We help buy people property who are in financial difficulty or who are needing to sell their property quickly for reasons such as death, divorce/separation, relocation, emigration.

We have a logo being designed incorporating strawberry and property (so red and green). We would like designs to communicate an elegant ,professional, approachable, friendly
fresh clean but also warm appealing appearance
Not too busy
Website consistent with logo and company name i.e. colour scheme

Please use our word document for content as a guide but use professional judgement for minor alterations if you feel they would benefit the site/structure etc

Please ask at any time if not sure

Target Market(s)

Adult british population, those that have a mortgage / loan / own property

Industry/Entity Type

Financial

Font styles to use
Serif
Sans Serif
Decorative

Colors
0692cd
33b7a4
acd036
fbee3e
3176b5
886aae
a6479a
e567a6
eb1f27

Requirements
Must have
• This must not look like a template website we are looking for UNIQUE please!
Nice to have
• Bristol pictures instead of generic, or colourful line drawings/comic drawings of houses/property/keys/happy people.....
Should not have
• An obvious off the shelf template design

```html
<!DOCTYPE html>
<html lang="en">
<head>
<meta charset="utf-8">
<title>Larkspur Homes</title>
<link href="https://fonts.googleapis.com/css2?family=Open+Sans:wght@400;600&family=Ubuntu:wght@400;500;700&display=swap" rel="stylesheet">
<style>
:root{
  --red:#c4121d;
  --red-dark:#b10f18;
  --red-light:#e0262f;
  --green:#7cb22e;
  --green-light:#a9d14d;
  --green-dark:#4e8a17;
  --text:#333;
  --muted:#777;
  --border:#d8d8d8;
  --footer-bg:#f1f1f3;
}
*{box-sizing:border-box;margin:0;padding:0}
html,body{width:1038px;height:1200px;overflow:hidden}
body{position:relative;background:#fff;font-family:"Open Sans",Arial,sans-serif;color:var(--text)}
.abs{position:absolute}
.top-rule{left:0;top:0;width:1038px;height:3px;background:#e3ecd7}
.hero-band{left:0;top:230px;width:1038px;height:116px;background:linear-gradient(#fff,#ececf1)}
.brand{left:78px;top:30px;font-family:"Ubuntu",sans-serif;font-weight:700;font-size:31px;color:var(--red);letter-spacing:.2px}
.slogan{left:81px;top:69px;font-size:13px;color:var(--green)}
.call{right:83px;top:39px;text-align:right}
.call-label{font-size:17px;color:var(--red);font-family:"Ubuntu",sans-serif}
.call-number{font-size:24px;color:var(--green);font-family:"Ubuntu",sans-serif;margin-top:1px;letter-spacing:.3px}
.main-nav{left:78px;top:102px;width:882px;height:45px;background:linear-gradient(var(--red-light),var(--red-dark));border-radius:4px 4px 0 0;display:flex}
.main-nav a{color:#fff;text-decoration:none;font-size:14.5px;font-weight:600;height:45px;line-height:45px;text-align:center;border-left:1px solid #a30d15;box-shadow:inset 1px 0 0 #e8434a}
.main-nav a:first-child{border-left:0;box-shadow:none}
.hero{left:78px;top:147px;width:882px;height:330px;background:#fff;border:1px solid var(--border);border-top:0;border-radius:0 0 5px 5px;overflow:hidden}
.hero-photo{position:absolute;left:372px;top:0;width:510px;height:330px;background:linear-gradient(100deg,rgba(255,255,255,0) 0%,#6c6f78 22%,#4a4d56 48%,#c9a27b 62%,#b9d4d8 80%,#dfecee 100%)}
.hero-photo::before{content:"";position:absolute;inset:0;background:linear-gradient(90deg,#fff 0%,rgba(255,255,255,0) 22%)}
.hero-title-small{left:49px;top:89px;font-family:"Ubuntu",sans-serif;font-size:23px;color:var(--red)}
.hero-title-large{left:49px;top:116px;font-family:"Ubuntu",sans-serif;font-size:30px;color:var(--red)}
.hero-text{left:51px;top:161px;width:360px;font-size:11.5px;line-height:19px;color:#999}
.dots{left:52px;top:205px;display:flex;gap:3px}
.dots span{width:11px;height:11px;border-radius:50%;background:#ccc}
.dots span:first-child{background:var(--green)}
.intro-title{left:82px;top:511px;font-family:"Ubuntu",sans-serif;font-size:21px;color:var(--red)}
.spec-list{list-style:none;font-size:12px;font-weight:600;color:#333}
.spec-list li{height:24px;line-height:18px;padding-left:11px;position:relative}
.spec-list li::before{content:"";position:absolute;left:0;top:5px;border-left:4px solid #ccc;border-top:4px solid transparent;border-bottom:4px solid transparent}
.help-box{left:81px;top:702px;width:609px;height:188px;border:1px solid var(--border);border-radius:3px;background:linear-gradient(#fff 60%,#f3f3f5)}
.help-title{position:absolute;left:27px;top:20px;font-family:"Ubuntu",sans-serif;font-size:21px;color:var(--green)}
.help-list{position:absolute;top:56px;list-style:none;font-size:12px;color:#555}
.help-list li{height:21.6px;padding-left:18px;position:relative}
.help-list svg{position:absolute;left:0;top:2px}
.contact-form{left:715px;top:502px;width:242px;height:297px;background:linear-gradient(var(--green-light),var(--green));border-radius:2px}
.form-title{position:absolute;left:21px;top:18px;font-family:"Ubuntu",sans-serif;font-size:21px;color:#fff}
.field{position:absolute;left:21px;width:201px;height:24px;background:#f4f4f4;border:1px solid #d6d6d6;border-radius:2px;font-size:10.5px;color:#777;padding:4px 10px}
.submit{position:absolute;left:21px;top:250px;width:87px;height:26px;background:var(--green-dark);color:#fff;font-size:12px;font-weight:600;text-align:center;line-height:26px}
.site-footer{left:0;top:923px;width:1038px;height:220px;border-top:1px solid #d4d4d4;background:linear-gradient(#fff,var(--footer-bg))}
.footer-col{position:absolute;top:30px}
.footer-col h3{font-family:"Ubuntu",sans-serif;font-weight:400;font-size:18px;color:var(--red);margin-bottom:4px}
.footer-col ul{list-style:none;font-size:12px;color:#444}
.footer-col li{height:23px;line-height:23px}
.contact-info p{font-size:12px;color:#444;height:23px;line-height:23px}
.contact-info .big{font-size:14px}
.badge{position:absolute;border-radius:4px}
.bottom-bar{left:0;top:1143px;width:1038px;height:57px;border-top:1px solid #ddd;background:#fff}
.copyright{position:absolute;left:86px;top:24px;font-size:11.5px;color:#666}
.social{position:absolute;top:15px;width:20px;height:20px;border-radius:2px}
</style>
</head>
<body>
<div class="abs top-rule"></div>
<div class="abs hero-band"></div>

<header>
  <div class="abs brand">Larkspur Homes</div>
  <div class="abs slogan">Your Slogan goes here</div>
  <div class="abs call">
    <div class="call-label">Call Us Now</div>
    <div class="call-number">0761 4830925</div>
  </div>
  <nav class="abs main-nav">
    <a href="#" style="width:77px">Home</a>
    <a href="#" style="width:172px">Sell Your Property Fast</a>
    <a href="#" style="width:181px">Rent Your Property Fast</a>
    <a href="#" style="width:133px">The 5 Easy Steps</a>
    <a href="#" style="width:154px">Common Questions</a>
    <a href="#" style="width:86px">About Us</a>
    <a href="#" style="width:79px">Contact</a>
  </nav>
</header>

<section class="abs hero">
  <div class="hero-photo" role="img" aria-label="Photo of a businessman in a suit signing a contract beside a small model house on a glass desk"></div>
  <div class="abs hero-title-small">Do you want to sell or rent</div>
  <div class="abs hero-title-large">out your house quickly?</div>
  <p class="abs hero-text">Aliquam nec erat at purus cursus interdum Vestibulum ligula augue bibendum accumsan vestibulum ut commodo a mi</p>
  <div class="abs dots"><span></span><span></span><span></span><span></span></div>
</section>

<h2 class="abs intro-title" style="font-weight:400">We are a local family run property business who specialize in</h2>
<ul class="abs spec-list" style="left:85px;top:555px">
  <li>Buying properties quickly</li>
  <li>Finding creative solutions to your property problems</li>
  <li>Property rental management</li>
  <li>Lettings to professional and student tenants</li>
  <li>Guaranteed rent and management schemes for landlords</li>
</ul>
<ul class="abs spec-list" style="left:454px;top:555px">
  <li>STOPPING repossessions</li>
  <li>Motivated sellers</li>
  <li>Chain fixing</li>
  <li>Negative equity problems</li>
</ul>

<section class="abs help-box">
  <h2 class="help-title" style="font-weight:400">Who can we help?</h2>
  <ul class="help-list" style="left:30px">
    <li><svg width="13" height="11" viewBox="0 0 13 11"><path d="M1 6l4 4 7-9" fill="none" stroke="#7cb22e" stroke-width="2.4"/></svg>How to stop repossession</li>
    <li><svg width="13" height="11" viewBox="0 0 13 11"><path d="M1 6l4 4 7-9" fill="none" stroke="#7cb22e" stroke-width="2.4"/></svg>Divorce or separaton</li>
    <li><svg width="13" height="11" viewBox="0 0 13 11"><path d="M1 6l4 4 7-9" fill="none" stroke="#7cb22e" stroke-width="2.4"/></svg>Financial Problems</li>
    <li><svg width="13" height="11" viewBox="0 0 13 11"><path d="M1 6l4 4 7-9" fill="none" stroke="#7cb22e" stroke-width="2.4"/></svg>Don't like estate agents?</li>
    <li><svg width="13" height="11" viewBox="0 0 13 11"><path d="M1 6l4 4 7-9" fill="none" stroke="#7cb22e" stroke-width="2.4"/></svg>Property needing work</li>
  </ul>
  <ul class="help-list" style="left:233px">
    <li><svg width="13" height="11" viewBox="0 0 13 11"><path d="M1 6l4 4 7-9" fill="none" stroke="#7cb22e" stroke-width="2.4"/></svg>Retiring landlords</li>
    <li><svg width="13" height="11" viewBox="0 0 13 11"><path d="M1 6l4 4 7-9" fill="none" stroke="#7cb22e" stroke-width="2.4"/></svg>Negative Equity</li>
    <li><svg width="13" height="11" viewBox="0 0 13 11"><path d="M1 6l4 4 7-9" fill="none" stroke="#7cb22e" stroke-width="2.4"/></svg>Opportunity not to be missed!!</li>
    <li><svg width="13" height="11" viewBox="0 0 13 11"><path d="M1 6l4 4 7-9" fill="none" stroke="#7cb22e" stroke-width="2.4"/></svg>Guaranteed rent scheme</li>
    <li><svg width="13" height="11" viewBox="0 0 13 11"><path d="M1 6l4 4 7-9" fill="none" stroke="#7cb22e" stroke-width="2.4"/></svg>Ill Health</li>
  </ul>
  <ul class="help-list" style="left:446px">
    <li><svg width="13" height="11" viewBox="0 0 13 11"><path d="M1 6l4 4 7-9" fill="none" stroke="#7cb22e" stroke-width="2.4"/></svg>Relocating</li>
    <li><svg width="13" height="11" viewBox="0 0 13 11"><path d="M1 6l4 4 7-9" fill="none" stroke="#7cb22e" stroke-width="2.4"/></svg>Inherited Property</li>
    <li><svg width="13" height="11" viewBox="0 0 13 11"><path d="M1 6l4 4 7-9" fill="none" stroke="#7cb22e" stroke-width="2.4"/></svg>Chain Collapse</li>
    <li><svg width="13" height="11" viewBox="0 0 13 11"><path d="M1 6l4 4 7-9" fill="none" stroke="#7cb22e" stroke-width="2.4"/></svg>Tenanted Property</li>
  </ul>
</section>

<aside class="abs contact-form">
  <h2 class="form-title" style="font-weight:400">CONTACT FORM</h2>
  <div class="field" style="top:55px">Name</div>
  <div class="field" style="top:85px">Email address</div>
  <div class="field" style="top:117px">Phone Number</div>
  <div class="field" style="top:148px">Property Address</div>
  <div class="field" style="top:181px;height:60px">Message</div>
  <div class="submit">SUBMIT</div>
</aside>

<footer class="abs site-footer">
  <div class="footer-col" style="left:91px">
    <h3>COMPANY</h3>
    <ul><li>Home</li><li>Sell Your Property Fast</li><li>Rent Your Property Fast</li><li>The 5 Easy Steps</li><li>Common Questions</li></ul>
  </div>
  <div class="footer-col" style="left:298px">
    <h3>ABOUT</h3>
    <ul><li>About Us</li><li>Sitemap</li><li>Our Services</li><li>Support</li><li>Contact Us</li></ul>
  </div>
  <div class="footer-col contact-info" style="left:443px">
    <h3>CONTACT INFO</h3>
    <p class="big">Larkspur Homes</p>
    <p>27 Orchard Lane, Unit 4</p>
    <p>Clifton BS8 4QT</p>
    <p class="big">0761 4830925</p>
    <p>info@larkspur-homes.co.uk</p>
  </div>
  <div class="badge" style="left:673px;top:40px;width:72px;height:92px;background:#222;border-radius:36px 36px 4px 4px"></div>
  <div class="badge" style="left:778px;top:48px;width:130px;height:34px;background:#1c2a3a"></div>
  <div class="badge" style="left:782px;top:100px;width:124px;height:43px;background:#183a8a;border-radius:2px"></div>
</footer>

<div class="abs bottom-bar">
  <div class="copyright">© 2014 Larkspur Homes Limited. Reg No 7731206</div>
  <div class="social" style="left:865px;background:#3b5b9a"></div>
  <div class="social" style="left:894px;background:#3fa9e0"></div>
  <div class="social" style="left:923px;background:#1e74b3"></div>
</div>
</body>
</html>
```